FC Varnet - Powerpoint for Sponsorship proposal

1. Introduction:
FC Varnet is seeking the development of a professional PowerPoint template to be used for club presentations, including the annual general meeting and sponsorship proposals. This template should reflect our club's identity, values, and colors, ideally incorporating the club's jersey colors.

2. Design Elements:

Color Scheme: The template should prominently feature FC Varnet's primary colors, which are red and blue, to create a strong visual association with the club.

Logo Integration: Include the club's logo in a tasteful and visible manner on each slide. The logo should be placed in a way that doesn't distract from the content but reinforces the club's identity.

Jersey Colors: If possible, incorporate the colors of the club's jerseys into the design elements or backgrounds to create a cohesive look.

3. Slide Layouts:
The template should include various slide layouts to accommodate the different sections of the presentations. Specific slide layouts should be designed for the following sections:

Title Slide: An impressive title slide with the club's logo, name, and potentially an image representing the club.

Objectives and Values: A clean and organized layout for presenting the club's objectives and core values.

Member Summary: A section for summarizing club members, categorized by type (e.g., players, coaches, volunteers).

Nationalities: A section for displaying a summary of the nationalities represented in the club.

Rankings Table: A visually appealing format for displaying league standings or rankings.

Committee Members: A slide template for introducing committee members, including their names, roles, and photos.

Financial Report: A structured layout for presenting financial data, including balance sheets and profit and loss statements.

Sponsorship Opportunities: A section for outlining the various sponsorship opportunities available, with clear details and benefits for potential sponsors.

4. Typography and Consistency:
Ensure that typography is consistent throughout the template, using easily readable fonts. Define font styles for headings, subheadings, and body text to maintain a professional look.

5. Imagery:
Incorporate high-quality images, such as action shots of matches or club events, to enhance the visual appeal of the template.

6. Simplicity and Clarity:
Maintain a clean, uncluttered design that prioritizes clarity and easy comprehension of the content. Avoid overly complex graphics or animations.

7. Customizability:
The template should be easily customizable, allowing presenters to add their content while preserving the overall design and branding.

8. Deliverables:
Provide the PowerPoint template in a format compatible with Microsoft PowerPoint.

Presentation to members or potential sponsors

Football

Sans Serif

0054AA
0677BA
7BADD7
CADEEF
E8F1F8
0094D4
00A9DD
6FCCEA
C7EBF8
E9F6FB
EB3D1F
EC4F4E
F09395
F8D3D4
FCEDEE

• See Project desscription

```html
<!DOCTYPE html>
<html lang="fr">
<head>
<meta charset="utf-8">
<title>FC Varnet – Dossier sponsoring 2022</title>
<link href="https://fonts.googleapis.com/css2?family=Poppins:wght@300;400;500;600;700&display=swap" rel="stylesheet">
<style>
:root{
  --red:#E8273B;
  --blue:#0A87C9;
  --navy:#0B1150;
  --mid-blue:#2B4C9B;
  --light-blue:#5B93D3;
  --pale-blue:#DDE8F3;
  --row-blue:#E3EDF7;
  --ink:#2A2A2A;
  --muted:#555;
  --map:#EEF0F2;
}
*{margin:0;padding:0;box-sizing:border-box}
html,body{width:1200px;height:1101px;overflow:hidden;background:#fff;font-family:"Poppins",sans-serif;color:var(--ink)}
.board{position:relative;width:1200px;height:1101px}
.slide{position:absolute;width:513px;height:288px;background:#fff;overflow:hidden;box-shadow:0 2px 10px rgba(0,0,0,.12)}
.s1{left:71px;top:64px}.s2{left:623px;top:64px}
.s3{left:71px;top:398px}.s4{left:623px;top:398px}
.s5{left:71px;top:733px}.s6{left:623px;top:733px}

.corner-blue{position:absolute;left:0;top:0;width:71px;height:68px;background:var(--blue)}
.corner-red{position:absolute;right:0;top:0;width:73px;height:68px;background:var(--red)}
.slide-title{position:absolute;left:0;right:0;top:14px;text-align:center;font-size:17px;font-weight:400;color:var(--ink)}
.title-rule{position:absolute;top:42px;left:50%;transform:translateX(-50%);width:64px;height:2px;display:flex;gap:4px}
.title-rule span{flex:1}
.title-rule span:first-child{background:var(--red)}
.title-rule span:last-child{background:var(--blue)}
.club-mark{position:absolute;left:6px;bottom:10px;display:flex;align-items:center;gap:4px;font-size:11px;font-weight:600;color:var(--ink)}
.club-mark i{width:9px;height:9px;background:var(--red);display:block}
.footer{position:absolute;left:184px;bottom:0;width:145px;height:20px;background:var(--red);clip-path:polygon(0 0,100% 0,88% 100%,12% 100%);color:#fff;font-size:7px;display:flex;align-items:center;justify-content:center}
.page-no{position:absolute;right:8px;bottom:9px;font-size:6.5px;color:var(--ink)}

/* Cover */
.cover-photo{position:absolute;inset:0;background:linear-gradient(135deg,#7d0d1c 0%,#c41d33 35%,#5a2b6b 60%,#0d4f8a 80%,#0a6aa8 100%)}
.cover-band{position:absolute;inset:0}
.cover-name{position:absolute;left:40px;top:62px;color:#fff;font-size:30px;font-weight:700;white-space:nowrap}
.cover-name i{display:inline-block;width:16px;height:16px;background:#fff;margin-right:9px;vertical-align:middle}
.cover-title{position:absolute;left:0;right:0;top:236px;text-align:center;color:#fff;font-size:17px;font-weight:600}
.cover-sub{position:absolute;left:0;right:0;top:262px;text-align:center;color:#fff;font-size:8.5px;font-weight:500}

/* Objectives */
.sub-head{position:absolute;left:0;right:0;text-align:center;font-weight:600;font-size:10px}
.lead{position:absolute;left:160px;width:193px;top:69px;text-align:center;font-size:5.2px;line-height:9px;color:var(--muted);font-weight:300}
.ring{position:absolute;width:64px;height:64px;border-radius:50%;border:1.2px solid var(--red);display:flex;align-items:center;justify-content:center;text-align:center;font-size:8px;line-height:11px;background:#fff}
.ring.blue{border-color:var(--blue)}
.pillar{position:absolute;width:135px;font-size:5.2px;line-height:9px;color:var(--muted);font-weight:300}
.pillar b{display:block;font-size:10px;line-height:13px;font-weight:600;color:var(--ink);margin-bottom:6px}
.pillar.left{left:30px;top:181px;text-align:right}
.pillar.right{left:319px;top:181px;text-align:left}

/* Nationalities */
.world-map{position:absolute;left:163px;top:66px;width:300px;height:192px;background:radial-gradient(ellipse at center,var(--map) 0%,#f7f8f9 70%,#fff 100%)}
.big-count{position:absolute;left:40px;width:120px;top:108px;text-align:center;font-size:50px;font-weight:700;line-height:1}
.big-label{position:absolute;left:30px;width:140px;top:164px;text-align:center;font-size:15px;font-weight:600}
.donut{position:absolute;left:205px;top:92px}
.legend{position:absolute;left:350px;top:98px;list-style:none}
.legend li{display:flex;align-items:center;gap:4px;font-size:11px;font-weight:600;height:26.5px;color:#333}
.legend span{width:7px;height:7px;display:block}

/* Staff */
.staff{position:absolute;left:22px;top:82px;display:flex;gap:6px}
.staff-card{position:relative;width:113px;height:135px;border-radius:4px;overflow:hidden;box-shadow:0 1px 4px rgba(0,0,0,.25)}
.staff-photo{position:absolute;inset:0;background:linear-gradient(180deg,#c9a98e 0%,#8a5f48 55%,#3a2420 100%)}
.staff-photo.kit{background:linear-gradient(180deg,#e9e9ea 0%,#b9b9bd 45%,#a8182b 75%,#4a0a14 100%)}
.staff-photo.dark{background:linear-gradient(180deg,#2a2a2a 0%,#151515 60%,#000 100%)}
.staff-info{position:absolute;left:0;right:0;bottom:18px;text-align:center;color:#fff}
.staff-info strong{display:block;font-size:9px;font-weight:600}
.staff-info small{display:block;font-size:5.8px;line-height:9px;font-weight:400}
.note{position:absolute;left:0;right:0;text-align:center;font-size:12px;font-weight:300;color:var(--ink)}

/* Tables */
.season{position:absolute;left:0;right:0;text-align:center;font-size:11px;font-weight:400}
.panel-table{position:absolute;left:73px;top:111px;width:368px;border-collapse:collapse;border:1.2px solid var(--navy);font-size:11px}
.panel-table th{background:var(--red);color:#fff;font-weight:400;height:30px;text-align:center}
.panel-table td{background:var(--row-blue);height:32px;border-top:1px solid #fff}
.panel-table td.type{padding-left:18px;width:130px}
.panel-table td.price{text-align:center}
.panel-table td.term{background:var(--blue);color:#fff;text-align:center;width:111px}
.offer-table{position:absolute;left:114px;top:63px;width:268px;table-layout:fixed;border-collapse:collapse;border:1.2px solid var(--navy);font-size:7.3px;font-weight:300}
.offer-table col.c-type{width:188px}
.offer-table col.c-price{width:80px}
.offer-table th{background:var(--red);color:#fff;font-weight:400;font-size:8px;height:22px;text-align:left;padding-left:26px}
.offer-table th.col-price{padding-left:0;text-align:center}
.offer-table td{background:var(--row-blue);height:18.7px;border-top:1px solid var(--navy);padding-left:14px;white-space:nowrap;overflow:hidden}
.offer-table td.amount{padding-left:4px}
</style>
</head>
<body>
<main class="board">

  <!-- Cover -->
  <section class="slide s1">
    <div class="cover-photo" role="img" aria-label="Photo d'un joueur en action dans un stade éclairé, teintée rouge et bleu"></div>
    <svg class="cover-band" width="513" height="288" viewBox="0 0 513 288" aria-hidden="true">
      <polygon points="0,288 513,0 513,12 20,288" fill="#fff"/>
    </svg>
    <div class="cover-name"><i></i>FC Varnet</div>
    <h1 class="cover-title">Dossier sponsoring 2022</h1>
    <p class="cover-sub">FC Varnet – 26 Août 2021</p>
  </section>

  <!-- Objectives -->
  <section class="slide s2">
    <div class="corner-blue"></div><div class="corner-red"></div>
    <h2 class="slide-title">Nos objectifs et motivations</h2>
    <div class="title-rule"><span></span><span></span></div>
    <p class="sub-head" style="top:50px">Le football pour progresser</p>
    <p class="lead">Promouvoir la relève locale pour nos équipes actives, filles et garçons. Former des éducateurs de qualité autour d'une philosophie commune sur l'aspect social et sportif. Aiguiller et accompagner les joueurs les plus talentueux sur la filière élite.</p>
    <div class="ring" style="left:162px;top:111px">… un club,<br>une famille</div>
    <div class="ring blue" style="left:225px;top:142px">… pour<br>progresser</div>
    <div class="ring" style="left:288px;top:111px">un club,<br>une famille</div>
    <div class="pillar left"><b>Le football<br>pour tous</b>Assurer l'accès pour tous, la cotisation doit rester peu onéreuse. Promouvoir le football féminin. Faciliter l'intégration par le football. Promouvoir le respect et le fair-play</div>
    <div class="pillar right"><b>Le football<br>pour tous</b>Assurer l'accès pour tous, la cotisation doit rester peu onéreuse. Promouvoir le football féminin. Faciliter l'intégration par le football. Promouvoir le respect et le fair-play</div>
    <div class="club-mark"><i></i>FC Varnet</div>
    <div class="footer">©2023. All rights reserved.</div>
    <div class="page-no">Page 02</div>
  </section>

  <!-- Nationalities -->
  <section class="slide s3">
    <div class="world-map" role="img" aria-label="Carte du monde en gris clair en arrière-plan"></div>
    <div class="corner-blue"></div><div class="corner-red"></div>
    <h2 class="slide-title">Le football, facteur d'intégration</h2>
    <div class="title-rule"><span></span><span></span></div>
    <div class="big-count">26</div>
    <div class="big-label">Nationalités</div>
    <svg class="donut" width="128" height="128" viewBox="0 0 128 128" role="img" aria-label="Répartition des nationalités : Suisse 62 %, Portugal 23 %, France 5 %, Autres 10 %">
      <g transform="rotate(-90 64 64)" fill="none" stroke-width="11">
        <circle cx="64" cy="64" r="53" stroke="var(--navy)" stroke-dasharray="206.5 333" stroke-dashoffset="0"/>
        <circle cx="64" cy="64" r="53" stroke="var(--mid-blue)" stroke-dasharray="76.6 333" stroke-dashoffset="-206.5"/>
        <circle cx="64" cy="64" r="53" stroke="var(--light-blue)" stroke-dasharray="16.6 333" stroke-dashoffset="-283.1"/>
        <circle cx="64" cy="64" r="53" stroke="var(--pale-blue)" stroke-dasharray="33.3 333" stroke-dashoffset="-299.7"/>
      </g>
      <g font-family="Poppins,sans-serif" font-size="5" fill="#fff">
        <text x="108" y="92">62%</text>
        <text x="6" y="77">23%</text>
        <text x="23" y="34">5%</text>
        <text x="41" y="15" fill="#333">10%</text>
      </g>
    </svg>
    <ul class="legend">
      <li><span style="background:var(--navy)"></span>Suisse</li>
      <li><span style="background:var(--mid-blue)"></span>Portugal</li>
      <li><span style="background:var(--light-blue)"></span>France</li>
      <li><span style="background:var(--pale-blue)"></span>Autres</li>
    </ul>
    <div class="club-mark"><i></i>FC Varnet</div>
    <div class="footer">©2023. All rights reserved.</div>
    <div class="page-no">Page 03</div>
  </section>

  <!-- Junior staff -->
  <section class="slide s4">
    <div class="corner-blue"></div><div class="corner-red"></div>
    <h2 class="slide-title">Encadrement junior</h2>
    <div class="title-rule"><span></span><span></span></div>
    <div class="staff">
      <article class="staff-card">
        <div class="staff-photo" role="img" aria-label="Portrait de l'entraîneur Luca Bernasconi"></div>
        <div class="staff-info"><strong>Luca Bernasconi</strong><small>Catégorie A, B, C</small></div>
      </article>
      <article class="staff-card">
        <div class="staff-photo kit" role="img" aria-label="Portrait de l'entraîneur Dario Ferri en maillot du club"></div>
        <div class="staff-info"><strong>Dario Ferri</strong><small>Catégorie C, D, E</small></div>
      </article>
      <article class="staff-card">
        <div class="staff-photo kit" role="img" aria-label="Portrait de l'entraîneur Moussa Diallo en maillot du club"></div>
        <div class="staff-info" style="bottom:9px"><strong>Moussa Diallo</strong><small>Catégorie C, D, E<br>Responsable Ecole fooot</small></div>
      </article>
      <article class="staff-card">
        <div class="staff-photo dark" role="img" aria-label="Portrait de l'entraîneur des gardiens Jan Weibel sur fond noir"></div>
        <div class="staff-info"><strong>Jan Weibel</strong><small>Responsable des gardiens</small></div>
      </article>
    </div>
    <p class="note" style="top:231px">Recherche d'une (éventuellement un) responsable du foot féminin</p>
    <div class="club-mark"><i></i>FC Varnet</div>
    <div class="footer">©2023. All rights reserved.</div>
    <div class="page-no">Page 04</div>
  </section>

  <!-- Boards -->
  <section class="slide s5">
    <div class="corner-blue"></div><div class="corner-red"></div>
    <h2 class="slide-title" style="top:16px">Sponsoring – Panneaux publicitaires</h2>
    <div class="title-rule" style="top:43px"><span></span><span></span></div>
    <p class="season" style="top:57px">Saison 2019/2020</p>
    <table class="panel-table">
      <thead><tr><th>Type</th><th>Par annee</th><th>Duree</th></tr></thead>
      <tbody>
        <tr><td class="type">Simple face</td><td class="price">445.-</td><td class="term" rowspan="2">5 ans</td></tr>
        <tr><td class="type">Double face</td><td class="price">545.-</td></tr>
      </tbody>
    </table>
    <p class="note" style="top:226px;left:92px;right:auto;text-align:left">Recherche d'une (éventuellement un) responsable du foot féminin</p>
    <div class="club-mark"><i></i>FC Varnet</div>
    <div class="footer">©2023. All rights reserved.</div>
    <div class="page-no">Page 05</div>
  </section>

  <!-- Other opportunities -->
  <section class="slide s6">
    <div class="corner-blue"></div><div class="corner-red"></div>
    <h2 class="slide-title" style="top:9px">Sponsoring – Autres opportunités</h2>
    <div class="title-rule" style="top:37px"><span></span><span></span></div>
    <p class="season" style="top:43px">Saison 2019/2020</p>
    <table class="offer-table">
      <colgroup><col class="c-type"><col class="c-price"></colgroup>
      <thead><tr><th>Type</th><th class="col-price">Par année</th></tr></thead>
      <tbody>
        <tr><td>Ballon d'Or</td><td class="amount">200.- / saison</td></tr>
        <tr><td>Ballon de match</td><td class="amount">100.- pour 1 match</td></tr>
        <tr><td>Ballon de match de coupe</td><td class="amount">150.- pour 1 match</td></tr>
        <tr><td>Carte supporter couple</td><td class="amount">150.- / saison</td></tr>
        <tr><td>Carte supporter simple</td><td class="amount">100.- / saison</td></tr>
        <tr><td>Tournoi Rivaz Cup – Logo sur affiche et internet</td><td class="amount">300.-</td></tr>
        <tr><td>Tournoi Rivaz Cup – Nom sur flyer</td><td class="amount">100.-</td></tr>
        <tr><td>Tournoi Memorial PLB – Logo sur affiche et internet</td><td class="amount">300.-</td></tr>
        <tr><td>Tournoi Mémorial PLB – Nom sur flyer</td><td class="amount">100.-</td></tr>
      </tbody>
    </table>
    <div class="club-mark"><i></i>FC Varnet</div>
    <div class="footer">©2023. All rights reserved.</div>
    <div class="page-no">Page 06</div>
  </section>

</main>
</body>
</html>
```